Front & Back Book Cover Design

Title:
THE QUIET LANDLORD: How to Grow Comfort and Plenty Through Property Held by Others
Author:
Mel T. Varnak
Design Philosophy:
A modern, minimalist-luxury aesthetic that feels visionary and intelligent — positioned between business innovation (The Brisk Venture), modern finance (The Anatomy of Thrift), and timeless real estate insight (Bold Aunt Meek Aunt).
Think: clean, bold, and idea-driven — a visual reflection of the book’s central concept: wealth through clarity, not clutter.
Back Cover:
To include book description along with author photo and bio
Files:
PNG, PDF, EPUB

```html
<!DOCTYPE html>
<html lang="en">
<head>
<meta charset="UTF-8">
<title>The Quiet Landlord — Mel T. Varnak</title>
<link rel="stylesheet" href="https://fonts.googleapis.com/css2?family=Archivo:wght@600&family=Arimo:wght@400&family=Montserrat:wght@600&display=swap">
<style>
  :root {
    --page: #ffffff;
    --cover-gold: #e2c262;
    --title-grey: #96979a;
    --title-black: #000000;
    --accent-red: #8b1a1e;
  }
  * { margin: 0; padding: 0; box-sizing: border-box; }
  html, body {
    width: 800px;
    height: 1200px;
    overflow: hidden;
    background: var(--page);
  }
  .book-cover {
    position: absolute;
    left: 37px;
    top: 55px;
    width: 726px;
    height: 1084px;
    background: var(--cover-gold);
  }
  .title-line {
    position: absolute;
    left: 0;
    width: 100%;
    text-align: center;
    font-family: "Archivo", "Helvetica Neue", Arial, sans-serif;
    font-weight: 600;
    line-height: 1;
    white-space: nowrap;
  }
  .title-article {
    top: 55px;
    font-size: 82px;
    color: var(--title-black);
  }
  .title-highlight {
    top: 134px;
    font-size: 125px;
    color: var(--title-grey);
  }
  .title-main {
    top: 248px;
    font-size: 125px;
    color: var(--title-black);
  }
  .subtitle {
    position: absolute;
    left: 0;
    top: 383px;
    width: 100%;
    text-align: center;
    font-family: "Arimo", Arial, sans-serif;
    font-size: 44px;
    line-height: 64px;
    letter-spacing: 4px;
    color: var(--accent-red);
  }
  .subtitle span { display: block; }
  .cover-emblem {
    position: absolute;
    left: 255px;
    top: 715px;
    width: 255px;
    height: 172px;
    background: linear-gradient(180deg, rgba(150,151,154,0.18), rgba(150,151,154,0.32));
  }
  .author-name {
    position: absolute;
    left: 0;
    top: 984px;
    width: 100%;
    text-align: center;
    font-family: "Montserrat", Arial, sans-serif;
    font-weight: 600;
    font-size: 57px;
    line-height: 1;
    letter-spacing: 12px;
    color: var(--accent-red);
    white-space: nowrap;
  }
</style>
</head>
<body>
  <main class="book-cover">
    <h1 class="book-title">
      <span class="title-line title-article">THE</span>
      <span class="title-line title-highlight">QUIET</span>
      <span class="title-line title-main">LANDLORD</span>
    </h1>
    <p class="subtitle">
      <span>How to Grow Comfort and</span>
      <span>Plenty Through Property</span>
      <span>Held by Others</span>
    </p>
    <div class="cover-emblem" role="img" aria-label="Thin grey line drawing of a modern building outline standing on a ground line"></div>
    <p class="author-name">MEL T. VARNAK</p>
  </main>
</body>
</html>
```